Inflatable Movie Screen company needs a Brochure Design for sales kit

We need a brochure as per attached sketch drawing which is to:
1)follow the sample layout
2) attached images must be used
3) to follow company corporate colors or suggest something professional and appropriate for the theme

Target Market(s)

Corporate and Community Clubs

Industry/Entity Type

Entertainment

Requirements
Must have
• Colors to be in line with corporate colors OR to suggest something appropriate.
Nice to have
• A unique concept
Should not have
• Too fanciful

```html
<!DOCTYPE html>
<html lang="en">
<head>
<meta charset="utf-8">
<title>Lumora Events – Inflatable Movie Screening Brochure</title>
<link href="https://fonts.googleapis.com/css2?family=Montserrat:ital,wght@0,400;0,500;0,600;1,300;1,400&display=swap" rel="stylesheet">
<style>
  :root{
    --backdrop:#8fbdce;
    --paper-top:#eef3f7;
    --paper-bottom:#cddce7;
    --valance:#f4f7fa;
    --valance-shade:#dbe6ee;
    --logo-box:#858688;
    --logo-text:#ffffff;
    --title:#5a5c60;
    --body:#5f6368;
    --rule:#9aa3ab;
    --quote-mark:#b9c2ca;
    --grass-light:#8fd14a;
    --grass-dark:#3f9a1f;
    --night-sky:#3e5274;
    --night-crowd:#1d2230;
  }
  *{margin:0;padding:0;box-sizing:border-box}
  html,body{width:1200px;height:1200px;overflow:hidden;background:var(--backdrop)}
  .spread{position:relative;width:1200px;height:1200px;font-family:"Montserrat",Arial,sans-serif}
  .page{position:absolute;top:230px;width:520px;height:740px;overflow:hidden;
        background:linear-gradient(180deg,var(--paper-top),var(--paper-bottom));
        box-shadow:0 6px 18px rgba(30,60,80,.25)}
  .page--cover{left:50px}
  .page--inner{left:630px}
  .page svg.art{position:absolute;inset:0;width:520px;height:740px}
  .brand-box{position:absolute;background:var(--logo-box);color:var(--logo-text);
             display:flex;flex-direction:column;align-items:center;justify-content:center;
             font-family:"Montserrat",Arial,sans-serif;font-weight:500;letter-spacing:.08em}
  .brand-box__name{line-height:1}
  .brand-box__legal{font-size:6px;letter-spacing:.12em;margin-top:4px}
  .page--cover .brand-box{left:190px;top:74px;width:140px;height:52px}
  .page--cover .brand-box__name{font-size:22px}
  .page--inner .brand-box{left:296px;top:96px;width:200px;height:72px}
  .page--inner .brand-box__name{font-size:32px}
  .page--inner .brand-box__legal{font-size:7px}
  .title{position:absolute;left:30px;top:40px;width:470px;text-align:right;
         font-size:25px;font-weight:500;color:var(--title);font-variant:small-caps;letter-spacing:.04em}
  .quote{position:absolute;font-style:italic;font-weight:300;font-size:12px;line-height:1.3;color:var(--body)}
  .quote cite{display:block;text-align:right;font-style:normal;font-weight:500;margin-top:3px}
  .quote--motto{left:352px;top:340px;width:160px;border-left:1px solid var(--rule);padding-left:8px}
  .quote--review{left:352px;top:545px;width:160px}
  .quote-mark{position:absolute;left:340px;top:492px;font-size:96px;line-height:1;font-weight:600;
              color:var(--quote-mark);font-style:normal}
</style>
</head>
<body>
<main class="spread">

  <section class="page page--cover">
    <svg class="art" viewBox="0 0 520 740">
      <defs>
        <radialGradient id="coverPhoto" cx="0.6" cy="0.45" r="0.7">
          <stop offset="0" stop-color="#c9ccd6"/>
          <stop offset="0.25" stop-color="#4d5a48"/>
          <stop offset="1" stop-color="#1f2a22"/>
        </radialGradient>
        <linearGradient id="grassCover" x1="0" y1="0" x2="0" y2="1">
          <stop offset="0" stop-color="var(--grass-light)"/>
          <stop offset="1" stop-color="var(--grass-dark)"/>
        </linearGradient>
      </defs>
      <circle cx="250" cy="375" r="205" fill="url(#coverPhoto)" role="img" aria-label="Photo of families seated on a lawn at night watching an inflatable outdoor movie screen"/>
      <path class="valance" fill="var(--valance)"
            d="M0,0 H520 V300 C500,270 470,250 440,268 C420,200 340,175 270,200 C230,150 170,170 140,200 C100,190 60,192 0,200 Z"/>
      <path fill="var(--valance-shade)" opacity=".6" d="M0,200 C60,192 100,190 140,200 C110,215 70,212 0,214 Z"/>
      <path fill="url(#grassCover)" role="img" aria-label="Green grass border"
            d="M0,640 C60,630 120,650 200,662 C280,675 360,690 430,700 C470,706 500,708 520,708 V740 H0 Z"/>
    </svg>
    <div class="brand-box"><span class="brand-box__name">LUMORA</span><span class="brand-box__legal">LUMORA EVENTS PTE LTD</span></div>
  </section>

  <section class="page page--inner">
    <svg class="art" viewBox="0 0 520 740">
      <defs>
        <linearGradient id="innerPhoto" x1="0" y1="0" x2="0" y2="1">
          <stop offset="0" stop-color="var(--night-sky)"/>
          <stop offset="0.45" stop-color="#5d7090"/>
          <stop offset="0.55" stop-color="#2f4a2e"/>
          <stop offset="0.7" stop-color="#3a2a2c"/>
          <stop offset="1" stop-color="var(--night-crowd)"/>
        </linearGradient>
        <linearGradient id="grassInner" x1="0" y1="0" x2="0" y2="1">
          <stop offset="0" stop-color="var(--grass-light)"/>
          <stop offset="1" stop-color="var(--grass-dark)"/>
        </linearGradient>
      </defs>
      <path fill="url(#innerPhoto)" role="img" aria-label="Photo of a large crowd on a park lawn at dusk facing a glowing inflatable movie screen beneath trees"
            d="M0,120 H330 C370,150 380,220 330,250 C300,330 320,430 330,520 C335,610 300,690 220,740 H0 Z"/>
      <path class="valance" fill="var(--valance)"
            d="M0,0 H520 V330 C500,300 470,250 420,240 C380,235 350,240 330,255 C300,180 240,150 180,175 C150,140 100,130 60,150 C40,140 20,140 0,145 Z"/>
      <path fill="var(--valance-shade)" opacity=".55" d="M330,255 C350,240 380,235 420,240 C470,250 500,300 520,330 V380 C490,330 440,290 380,280 C355,276 338,270 330,255 Z"/>
      <path fill="url(#grassInner)" role="img" aria-label="Green grass border"
            d="M150,720 C230,700 300,706 380,716 C430,722 480,730 520,734 V740 H150 Z"/>
    </svg>
    <h1 class="title">Inflatable Movie Screening</h1>
    <div class="brand-box"><span class="brand-box__name">LUMORA</span><span class="brand-box__legal">LUMORA EVENTS PTE LTD</span></div>
    <blockquote class="quote quote--motto">Of all of our inventions for mass communication, pictures still speak the most universally understood language.<cite>-Harold Vance</cite></blockquote>
    <span class="quote-mark" aria-hidden="true">&ldquo;</span>
    <blockquote class="quote quote--review">Enjoyed watching [movie name] with my family. It was nice to get away from the usual malls and bond together. My kids loved it!<cite>-Mei Tan, housewife</cite></blockquote>
  </section>

</main>
</body>
</html>
```